Zielgruppe
Wir sind ein Restaurant und starten jetzt mit der Herstellung von eigenen Getränken wie z.B. Whisky, Gin, Rum, Weine, Liköre etc. Die erste Linie des Whiksy haben wir selbst entworfen möchten aber mehr Professionalität einbringen.
Aufgabenstellung
Beiliegend die beiden Flaschen welche bedruckt/beklebt werden (mit Flaschenbezeichnung) und unser LOGO als PSD.
Stichworte: Regional, Qualität, Beste Zutaten, keine Zusatzstoffe
Bezeichnungen: Silberfalter Whisky / Silberfalter Gin
Wichtig: Wiederkennungswert schaffen (Es sollen in Zukunft auch Weine, Liköre etc. produziert werden)
Infos Gin:
- 65 verschiedenen Botanicals
- Neben Blutorangen, Zitronen und Limetten, zeigt auch der Duft von Ingwer, Zitronengras und Kaffirlimettenblätter als Zitrusensemble das Facettenreichtum des Gins. Das Aromaspiel verändert sich nach etwas Zeit im Glas sehr deutlich. Dann zeigen sich starke Aromakomponenten wie Kardamom, Koriander oder Piment. Der Gin zeichnet sich aus durch seine Lebendigkeit
- 42%vol
- 500ml
Infos Whisky:
- 8 Jahre gereift
- Zur Vergärung unseres Whiskys verwenden wir eigens gezüchtete Frischhefe mit besonderen Fähigkeiten zur Bildung von sehr fruchtigen Gäraromen. Die Weichheit bekommt er durch die dreifache Destillation. Auch bei der Wahl unserer Gerste setzen wir auf unsere Region. Der Grund für diesen starken regionalen Bezug ist, dass wir versuchen unserem Whisky die größtmögliche Portion an Terroir zu verleihen. Bei der anschließenden Fasslagerung setzen wir auf hochwertige Fässer. Zuerst neue amerikanische Weißeiche mit anschließendem Sherry- und Cognacfass finish.
Tradition und Moderne verschmelzen zu einem unverwechselbaren Whisky, mit weichem, fruchtigen femininen Geschmack und wildem, maskulinen Charakter.
- Single Malt Whisky
- Geruch & Geschmack: Der Whisky zeichnet sich aus durch intensive, weiche Aromen nach Vanille und süßen Früchten, mit einem ungewöhnlich weichen und sanften Abgang mit einem Hauch von dunkler Schokolade.
Folgende obligatorischen Angaben sind Pflicht:
- Adresse 'Silberfalter / Lindenwiese 7 / 48213 Linkenheim-Hochstetten'
- Losnummer z.B. L0121..

```html
<!DOCTYPE html>
<html lang="en">
<head>
<meta charset="utf-8">
<title>Silberfalter Gin &amp; Whiskey Labels</title>
<link rel="stylesheet" href="https://fonts.googleapis.com/css2?family=Mr+De+Haviland&family=Pinyon+Script&family=Tinos&display=swap">
<style>
  :root {
    --backdrop: #f6f6f5;
    --label-dark: #0e0e0e;
    --label-mid: #2a2928;
    --label-light: #4b4946;
    --gold: #d6ab2a;
    --ink-white: #f2f2f2;
    --volume-grey: #a8a6a2;
  }
  * { margin: 0; padding: 0; box-sizing: border-box; }
  html, body {
    width: 1200px;
    height: 849px;
    overflow: hidden;
    background: var(--backdrop);
  }
  .canvas {
    position: relative;
    width: 1200px;
    height: 849px;
  }
  .label {
    position: absolute;
    top: 324px;
    width: 215px;
    height: 408px;
    overflow: hidden;
    background: linear-gradient(90deg, var(--label-dark) 0%, var(--label-mid) 55%, var(--label-light) 100%);
    border-radius: 6px 6px 30px 30px;
  }
  .label--gin { left: 328px; }
  .label--whiskey { left: 670px; }

  .brand-ring {
    position: absolute;
    top: 63px;
    left: 74px;
    width: 67px;
    height: 67px;
    border: 1.5px solid var(--gold);
    border-radius: 50%;
  }
  .brand-name {
    position: absolute;
    top: 136px;
    left: 0;
    width: 100%;
    text-align: center;
    font-family: "Mr De Haviland", cursive;
    font-size: 34px;
    line-height: 1;
    color: var(--gold);
  }
  .product-name {
    position: absolute;
    top: 178px;
    left: 0;
    width: 100%;
    text-align: center;
    font-family: "Pinyon Script", cursive;
    line-height: 80px;
    height: 80px;
    color: var(--gold);
    white-space: nowrap;
  }
  .label--gin .product-name { font-size: 58px; }
  .label--whiskey .product-name { font-size: 46px; }

  .tasting-notes {
    position: absolute;
    top: 272px;
    left: 8px;
    width: 199px;
    transform: rotate(-4deg);
    transform-origin: center;
    font-family: "Mr De Haviland", cursive;
    font-size: 12px;
    line-height: 13px;
    color: var(--ink-white);
    white-space: nowrap;
  }
  .tasting-notes .headline {
    text-align: center;
  }
  .volume {
    position: absolute;
    top: 364px;
    left: 0;
    width: 100%;
    text-align: center;
    font-family: "Tinos", serif;
    font-size: 11.5px;
    color: var(--volume-grey);
  }
  .volume .divider {
    display: inline-block;
    width: 1px;
    height: 13px;
    margin: 0 3px;
    vertical-align: -2px;
    background: var(--volume-grey);
  }
</style>
</head>
<body>
<main class="canvas">

  <section class="label label--gin">
    <div class="brand-ring"></div>
    <p class="brand-name">Silberfalter</p>
    <p class="product-name">Gin</p>
    <div class="tasting-notes">
      <p class="headline">- 65 different botanicals</p>
      <p>Blood oranges, lemons and limes, ginger and</p>
      <p>lemongrass with kaffir lime leaves show the</p>
      <p>many facets of gin. The play of aromas changes</p>
      <p>in the glass. Then cardamom, coriander or</p>
      <p>allspice appear. A gin full of liveliness.</p>
    </div>
    <p class="volume">42% vol<span class="divider"></span>500ml</p>
  </section>

  <section class="label label--whiskey">
    <div class="brand-ring"></div>
    <p class="brand-name">Silberfalter</p>
    <p class="product-name">Whiskey</p>
    <div class="tasting-notes">
      <p class="headline">- 65 different botanicals</p>
      <p>Blood oranges, lemons and limes, ginger and</p>
      <p>lemongrass with kaffir lime leaves show the</p>
      <p>many facets of gin. The play of aromas changes</p>
      <p>in the glass. Then cardamom, coriander or</p>
      <p>allspice appear. A gin full of liveliness.</p>
    </div>
    <p class="volume">42% vol<span class="divider"></span>500ml</p>
  </section>

</main>
</body>
</html>
```